Heron Hotel - Weekly Events Calendar

I run a hotel property in Barbados called the Pelmont (www.thepelmont-stay.example) and we need some flyer templates preparing that we can use weekly on site at the hotel. They need to carry some logo branding but we can keep the balance reasonably informal, however they do need to be able to be edited by our staff easily to fill with the various content each week.
We need three templates, one for our sports bar, one for the music acts we put on in Bar2350 and then one that summarises all the activities each day on site.
I've uploaded a sketch that covers this in more detail.
ideally we use these flyers in a few different ways. We can push them on our app (the Pelmont Resort on the app store), via physical posters and digital posters around site, and on table top paper stands at various outlets.

Keen to see something creative yet simple, and something we can update easily ourselves with content

Target Market(s)

Hotel guests

Colors
0054AA
0677BA
7BADD7
CADEEF
E8F1F8
0094D4
00A9DD
6FCCEA
C7EBF8
E9F6FB

Requirements
Must have
• the ability to be edited each day/week by my team - so likely PPT or word format

```html
<!DOCTYPE html>
<html lang="en">
<head>
<meta charset="utf-8">
<title>The Pelmont – Weekly Events Flyers</title>
<link href="https://fonts.googleapis.com/css2?family=PT+Serif:wght@400;700&family=Roboto:wght@400;700&display=swap" rel="stylesheet">
<style>
  :root {
    --brand-blue: #0054AA;
    --sky: #6FCCEA;
    --backdrop: #d5d6d8;
    --paper: #ffffff;
    --ink: #1b1b1b;
    --spa-ink: #0d2440;
    --rule: #2f6fc0;
  }
  * { box-sizing: border-box; margin: 0; padding: 0; }
  html, body { width: 1200px; height: 909px; overflow: hidden; }
  body {
    background: var(--backdrop);
    font-family: "Roboto", Arial, sans-serif;
    position: relative;
  }
  .flyer {
    position: absolute;
    top: 68px;
    width: 546px;
    height: 772px;
    background: var(--paper);
    overflow: hidden;
  }
  .flyer--summary { left: 44px; }
  .flyer--bar { left: 623px; }

  /* Brand name */
  .brand-name {
    position: absolute;
    text-align: center;
    font-family: "PT Serif", Georgia, serif;
    font-weight: 400;
    white-space: nowrap;
  }
  .summary-brand {
    left: 20px; top: 26px; width: 236px;
    font-size: 34px; line-height: 44px;
    color: var(--brand-blue);
  }
  .bar-brand {
    left: 0; top: 44px; width: 260px;
    font-size: 42px; line-height: 52px;
    color: #fff;
  }
  .header-divider {
    position: absolute;
    left: 270px; top: 19px;
    width: 1.5px; height: 58px;
    background: var(--brand-blue);
  }
  .summary-title {
    position: absolute;
    left: 301px; top: 32px;
    font-family: "PT Serif", Georgia, serif;
    font-weight: 700;
    font-size: 26px;
    color: var(--brand-blue);
    letter-spacing: 0.3px;
  }

  /* Event tiles */
  .tile { position: absolute; width: 255px; height: 245px; }
  .tile--music { left: 10px; top: 102px; }
  .tile--sports { left: 276px; top: 102px; }
  .tile--yoga { left: 10px; top: 359px; }
  .tile--cooking { left: 276px; top: 359px; }
  .tile__photo {
    height: 131px;
    display: flex;
    align-items: center;
    justify-content: center;
  }
  .tile__label {
    font-family: "PT Serif", Georgia, serif;
    font-size: 22px;
    color: #fff;
    white-space: nowrap;
  }
  .photo--music { background: linear-gradient(135deg, #3a2f1a 0%, #1e1d22 45%, #23232a 100%); }
  .photo--sports { background: linear-gradient(160deg, #3e3b36 0%, #23241f 55%, #1b1c18 100%); }
  .photo--yoga { background: linear-gradient(180deg, #3a3b40 0%, #5a4a47 55%, #2a2627 100%); }
  .photo--cooking { background: linear-gradient(150deg, #55565a 0%, #34302c 55%, #4c4b4d 100%); }
  .tile__info {
    height: 114px;
    background: var(--brand-blue);
    color: #fff;
    padding: 21px 0 0 24px;
  }
  .tile__date { font-size: 14px; line-height: 18px; }
  .tile__event {
    font-family: "PT Serif", Georgia, serif;
    font-size: 18px;
    line-height: 24px;
    margin-top: 3px;
  }
  .tile__time { font-size: 14px; line-height: 18px; margin-top: 4px; white-space: nowrap; }
  .tile__time strong { font-weight: 700; }
  .fixture { display: flex; gap: 12px; margin-top: 10px; }

  /* Spa band */
  .spa {
    position: absolute;
    left: 0; top: 621px;
    width: 546px; height: 151px;
    background: var(--sky);
  }
  .spa__photo {
    position: absolute;
    left: 12px; top: 11px;
    width: 197px; height: 131px;
    background: linear-gradient(135deg, #5f7681 0%, #c8c2b6 50%, #6a7f88 100%);
  }
  .spa__copy { position: absolute; left: 239px; top: 24px; color: var(--spa-ink); }
  .spa__heading, .spa__offer {
    font-family: "PT Serif", Georgia, serif;
    font-weight: 400;
    font-size: 21px;
    line-height: 28px;
  }
  .spa__offer { margin-top: 6px; }
  .spa__text { font-size: 14px; line-height: 20px; margin-top: 6px; }

  /* Bar flyer */
  .bar-photo {
    position: absolute;
    left: 0; top: 0;
    width: 260px; height: 772px;
    background: linear-gradient(160deg, #4a2a16 0%, #7a4220 30%, #2a1a10 60%, #0e0a08 100%);
  }
  .venue-name {
    position: absolute;
    left: 0; top: 650px;
    width: 260px;
    text-align: center;
    font-family: "PT Serif", Georgia, serif;
    font-size: 34px;
    color: #fff;
  }
  .schedule { position: absolute; left: 260px; top: 0; width: 286px; height: 772px; }
  .schedule__rule {
    position: absolute;
    left: 0; width: 286px; height: 1px;
    background: var(--rule);
  }
  .schedule__dot {
    position: absolute;
    left: -4px; top: -4px;
    width: 9px; height: 9px;
    border-radius: 50%;
    background: var(--brand-blue);
  }
  .night { position: absolute; left: 42px; }
  .night__date { font-size: 14px; line-height: 18px; color: var(--ink); }
  .night__act {
    font-family: "PT Serif", Georgia, serif;
    font-size: 19px;
    line-height: 24px;
    color: var(--brand-blue);
    margin-top: 3px;
  }
  .night__time { font-size: 14px; line-height: 18px; color: var(--ink); margin-top: 3px; }
</style>
</head>
<body>

<section class="flyer flyer--summary">
  <div class="brand-name summary-brand">The Pelmont</div>
  <div class="header-divider"></div>
  <h1 class="summary-title">DAILY SUMMARY</h1>

  <article class="tile tile--music">
    <div class="tile__photo photo--music" role="img" aria-label="Close-up of hands playing a bass guitar">
      <span class="tile__label">MUSIC</span>
    </div>
    <div class="tile__info">
      <p class="tile__date">Monday 17 June</p>
      <p class="tile__event">LOREM IPSUM</p>
      <p class="tile__time">LIVE FROM 7:00 PM</p>
    </div>
  </article>

  <article class="tile tile--sports">
    <div class="tile__photo photo--sports" role="img" aria-label="Football players' legs competing for the ball">
      <span class="tile__label">SPORTS</span>
    </div>
    <div class="tile__info">
      <p class="tile__date">Monday 17 June</p>
      <p class="tile__event">FOOTBALL</p>
      <p class="tile__time fixture"><span>MARINERS</span><strong>7:00 PM</strong><span>CORALS</span></p>
    </div>
  </article>

  <article class="tile tile--yoga">
    <div class="tile__photo photo--yoga" role="img" aria-label="Silhouette of a person in a yoga pose at sunset by the sea">
      <span class="tile__label">YOGA CLASSES</span>
    </div>
    <div class="tile__info">
      <p class="tile__date">Monday 17 June</p>
      <p class="tile__event">LOREM IPSUM</p>
      <p class="tile__time">LIVE FROM 7:00 PM</p>
    </div>
  </article>

  <article class="tile tile--cooking">
    <div class="tile__photo photo--cooking" role="img" aria-label="Stir-fried rice being tossed in a pan">
      <span class="tile__label">COOKING EVENTS</span>
    </div>
    <div class="tile__info">
      <p class="tile__date">Monday 17 June</p>
      <p class="tile__event">NOODLES</p>
      <p class="tile__time">Starting&nbsp; <strong>7:00 PM</strong></p>
    </div>
  </article>

  <aside class="spa">
    <div class="spa__photo" role="img" aria-label="Guest relaxing during a spa massage treatment"></div>
    <div class="spa__copy">
      <h2 class="spa__heading">SPA DEALS</h2>
      <p class="spa__offer">15% OFF on Monday</p>
      <p class="spa__text">Lorem Ipsum is simply dummy&nbsp; text<br>of the printing</p>
    </div>
  </aside>
</section>

<section class="flyer flyer--bar">
  <div class="bar-photo" role="img" aria-label="Close-up of hands playing an acoustic guitar"></div>
  <div class="brand-name bar-brand">The Pelmont</div>
  <div class="venue-name">Bar2350</div>

  <div class="schedule">
    <div class="night" style="top:28px">
      <p class="night__date">Monday 17 June</p>
      <p class="night__act">LOREM IPSUM</p>
      <p class="night__time">LIVE FROM 7:00 PM</p>
    </div>
    <div class="schedule__rule" style="top:116px"><span class="schedule__dot"></span></div>
    <div class="night" style="top:137px">
      <p class="night__date">Tuesday 18 June</p>
      <p class="night__act">LOREM IPSUM</p>
      <p class="night__time">LIVE FROM 7:00 PM</p>
    </div>
    <div class="schedule__rule" style="top:219px"><span class="schedule__dot"></span></div>
    <div class="night" style="top:241px">
      <p class="night__date">Wednesday 19 June</p>
      <p class="night__act">LOREM IPSUM</p>
      <p class="night__time">LIVE FROM 7:00 PM</p>
    </div>
    <div class="schedule__rule" style="top:324px"><span class="schedule__dot"></span></div>
    <div class="night" style="top:345px">
      <p class="night__date">Thursday 20 June</p>
      <p class="night__act">LOREM IPSUM</p>
      <p class="night__time">LIVE FROM 7:00 PM</p>
    </div>
    <div class="schedule__rule" style="top:428px"><span class="schedule__dot"></span></div>
    <div class="night" style="top:449px">
      <p class="night__date">Friday 19 June</p>
      <p class="night__act">LOREM IPSUM</p>
      <p class="night__time">LIVE FROM 7:00 PM</p>
    </div>
    <div class="schedule__rule" style="top:535px"><span class="schedule__dot"></span></div>
    <div class="night" style="top:553px">
      <p class="night__date">Saturday 20 June</p>
      <p class="night__act">LOREM IPSUM</p>
      <p class="night__time">LIVE FROM 7:00 PM</p>
    </div>
    <div class="schedule__rule" style="top:639px"><span class="schedule__dot"></span></div>
    <div class="night" style="top:668px">
      <p class="night__date">Sunday 21 June</p>
      <p class="night__act">LOREM IPSUM</p>
      <p class="night__time">LIVE FROM 7:00 PM</p>
    </div>
  </div>
</section>

</body>
</html>
```